Powerpoint template for corporate presentations

Our company, MeridianQuillworks, has recently undertaken a re-branding overhaul for our website and corporate materials (color scheme, letterhead, biz cards). In support of this re-branding effort, we need a powerpoint template for corporate presentations that will reflect the look and feel of the website.

We would like to receive a powerpoint template that contains the following slide layouts:
- title slide
- section header slide
- content slide (title & content)
- closing/acknowledgement slide

The website design, colors, fonts and images are included as attachments for your reference.An example powerpoint template is included, if needed for your reference. We would like to see the icons and colors used to make the presentation more visually appealing.

Specific comments regarding the example ppt with content attached to this brief:
- the content slides seem a bit sparse and do not have much space for text/charts.
- For the content slides, a white/light background and dark text is still expected.
- For the section header and closing slides, we would like to see a layout more engaging than just the blue background. Note: a blue or colored background is acceptable for these slides so long as the text color has enough contrast to be visible.

```html
<!DOCTYPE html>
<html lang="en">
<head>
<meta charset="UTF-8">
<title>MeridianQuillworks – Content Slide</title>
<link rel="stylesheet" href="https://fonts.googleapis.com/css2?family=Open+Sans:wght@300;400;600;700&display=swap">
<style>
  :root {
    --brand-cyan: #00b6eb;
    --accent-yellow: #f6b90f;
    --ink: #1d1d1d;
    --body-text: #333333;
    --muted: #b8b8b8;
    --rule: #bfbfbf;
    --figure-fill: #d9ecf4;
    --paper: #ffffff;
  }
  * { margin: 0; padding: 0; box-sizing: border-box; }
  html, body { width: 1200px; height: 900px; overflow: hidden; background: var(--paper); }
  .slide {
    position: relative;
    width: 1200px;
    height: 900px;
    background: var(--paper);
    font-family: "Open Sans", Arial, sans-serif;
  }
  .title-bar {
    position: absolute; left: 0; top: 0;
    width: 1200px; height: 95px;
    background: var(--brand-cyan);
    border-bottom: 5px solid var(--accent-yellow);
  }
  .slide-title {
    position: absolute; left: 33px; top: 22px;
    font-size: 42px; font-weight: 600; letter-spacing: 0.5px;
    color: var(--ink); line-height: 1.2;
  }
  .audience {
    position: absolute; left: 50px; top: 203px; width: 252px;
  }
  .audience-figure {
    display: block; margin: 0 auto;
    width: 232px; height: 232px;
    background: linear-gradient(180deg, #eef3f5 0%, var(--figure-fill) 60%, #37b4df 100%);
    border-radius: 6px;
  }
  .audience-label {
    margin-top: 5px;
    border-top: 1.5px solid var(--rule);
    border-bottom: 1.5px solid var(--rule);
    padding: 4px 0 5px;
    text-align: center;
    color: var(--brand-cyan);
    font-size: 22px; line-height: 28px;
  }
  .points {
    position: absolute; left: 396px; top: 230px;
    list-style: none;
  }
  .points li {
    display: flex; align-items: center;
    height: 34px; margin-bottom: 50px;
    font-size: 22px; color: var(--body-text);
  }
  .points svg { width: 18px; height: 20px; margin-right: 10px; flex: none; }
  .footer-rule {
    position: absolute; left: 0; top: 814px;
    width: 1200px; height: 3px; background: var(--accent-yellow);
  }
  .brand-name {
    position: absolute; left: 30px; top: 828px;
    font-size: 45px; font-weight: 300; color: var(--brand-cyan);
    line-height: 60px; letter-spacing: 1px;
  }
  .copyright {
    position: absolute; right: 21px; top: 848px;
    font-size: 21px; color: var(--muted);
  }
</style>
</head>
<body>
<main class="slide">
  <header class="title-bar">
    <h1 class="slide-title">PROJECT TITLE HERE</h1>
  </header>

  <section class="audience">
    <div class="audience-figure" role="img" aria-label="Icon of a person representing patients and families"></div>
    <p class="audience-label">PATIENTS AND<br>FAMILIES</p>
  </section>

  <ul class="points">
    <li><svg viewBox="0 0 18 20" aria-hidden="true"><path d="M3 2 L11 10 L3 18 L7 18 L15 10 L7 2 Z" fill="var(--brand-cyan)"/></svg>Patients and families can join a registry to submit their own data.</li>
    <li><svg viewBox="0 0 18 20" aria-hidden="true"><path d="M3 2 L11 10 L3 18 L7 18 L15 10 L7 2 Z" fill="var(--brand-cyan)"/></svg>All it takes is a few web surveys and the public data can be explored.</li>
    <li><svg viewBox="0 0 18 20" aria-hidden="true"><path d="M3 2 L11 10 L3 18 L7 18 L15 10 L7 2 Z" fill="var(--brand-cyan)"/></svg>More surveys completed = more data patients and families can view.</li>
  </ul>

  <div class="footer-rule"></div>
  <footer>
    <p class="brand-name">MeridianQuillworks</p>
    <p class="copyright">Copyright text here</p>
  </footer>
</main>
</body>
</html>
```